Business Card Design using new attached logo

We are a family run Plumbing and Heating firm looking to improve our company image with an improved business card and new logo.We are looking to keep the company colour (Blue) involved in our design

Reason: New logo added which needs to be incorporated on designs

Industry/Entity Type

Business

Contact Information for Business Card

See attachment of all info required.

Requirements
Must have
• We have just picked a new company logo which is attached.
• Could you please provide your business card designs using this logo.
• We are looking for the logo on the back as well as the front with all the info required

```html
<!DOCTYPE html>
<html lang="en">
<head>
<meta charset="utf-8">
<title>Kestrel Services – Business Card</title>
<link href="https://fonts.googleapis.com/css2?family=Cinzel:wght@600&family=Source+Sans+3:ital,wght@0,400;0,600;1,400&display=swap" rel="stylesheet">
<style>
  :root {
    --stage: #333333;
    --blue-light: #3b88cb;
    --blue-mid: #2a5ea8;
    --blue-deep: #1d3674;
    --navy-text: #2b3d78;
    --white: #ffffff;
    --paper: #ffffff;
  }
  * { margin: 0; padding: 0; box-sizing: border-box; }
  html, body {
    width: 1200px; height: 907px; overflow: hidden;
    background: var(--stage);
    font-family: "Source Sans 3", "Myriad Pro", sans-serif;
  }
  .card {
    position: absolute; left: 300px; width: 601px; height: 343px;
    box-shadow: 0 3px 8px rgba(0,0,0,0.55);
  }
  .card--front {
    top: 92px;
    background: radial-gradient(ellipse 360px 260px at 318px 166px,
      var(--blue-light) 0%, var(--blue-mid) 45%, var(--blue-deep) 100%);
    color: var(--white);
  }
  .card--back { top: 472px; background: var(--paper); }

  .brand {
    position: absolute; font-weight: 600; letter-spacing: 1px;
    display: flex; align-items: center; gap: 10px; white-space: nowrap;
  }
  .brand__dot { width: 14px; height: 14px; border-radius: 50%; background: currentColor; }
  .card--front .brand { right: 45px; top: 58px; font-size: 30px; color: var(--white); }
  .card--back .brand {
    left: 0; right: 0; justify-content: center; top: 145px;
    font-size: 38px; color: var(--blue-mid);
  }

  .holder { position: absolute; left: 42px; top: 120px; font-family: "Cinzel", serif; font-weight: 600; }
  .holder__name { font-size: 22px; letter-spacing: 0.5px; line-height: 1; }
  .holder__role { font-size: 17px; margin-top: 11px; line-height: 1; }
  .rule { position: absolute; left: 42px; right: 45px; top: 184px; height: 1px; background: var(--white); }

  .contacts { position: absolute; left: 42px; top: 196px; list-style: none; font-size: 15px; }
  .contacts li { display: flex; align-items: center; height: 24px; }
  .contacts svg { width: 14px; height: 14px; margin-right: 11px; fill: var(--white); flex: none; }

  .address {
    position: absolute; right: 45px; top: 229px; text-align: right;
    font-size: 15px; line-height: 22px; font-style: normal;
  }
  .tagline {
    position: absolute; left: 0; right: 0; top: 284px; text-align: center;
    font-style: italic; font-size: 16px; color: var(--navy-text);
  }
</style>
</head>
<body>
  <section class="card card--front">
    <div class="brand"><span class="brand__dot"></span>KESTREL SERVICES</div>
    <div class="holder">
      <p class="holder__name">Daniel Hartley</p>
      <p class="holder__role">Director</p>
    </div>
    <div class="rule"></div>
    <ul class="contacts">
      <li><svg viewBox="0 0 16 16" aria-hidden="true"><path d="M3 1l3 3-1.5 2c1 2 3 4 5 5l2-1.5 3 3-2 2C7 14 2 9 1 3z"/></svg>020 7946 0321</li>
      <li><svg viewBox="0 0 16 16" aria-hidden="true"><path d="M4 1h8v4H4zM1 6h14v6h-2v3H3v-3H1zm4 4v3h6v-3z"/></svg>020 7946 0458</li>
      <li><svg viewBox="0 0 16 16" aria-hidden="true"><path d="M4 0h8v16H4zm1 2v6h6V2zm0 8v4h6v-4z"/></svg>07700900417</li>
      <li><svg viewBox="0 0 16 16" aria-hidden="true"><path d="M1 3h14v10H1zm1 1.5v.5l6 4 6-4v-.5z"/></svg>danielhartley@kestrelservicesltd.co.uk</li>
      <li><svg viewBox="0 0 16 16" aria-hidden="true"><path d="M8 1a7 7 0 100 14A7 7 0 008 1zm0 1.3c.9 1.2 1.4 2.6 1.6 4.2H6.4C6.6 4.9 7.1 3.5 8 2.3zM2.4 7.5h2.8c.1 1.6.5 3 1.2 4.2A5.7 5.7 0 012.4 7.5zm4 0h3.2c-.1 1.6-.7 3-1.6 4.2-.9-1.2-1.5-2.6-1.6-4.2zm4.4 0h2.8a5.7 5.7 0 01-4 4.2c.7-1.2 1.1-2.6 1.2-4.2zM2.5 6.5a5.7 5.7 0 013.9-4c-.7 1.2-1.1 2.5-1.2 4zm8.3 0c-.1-1.5-.5-2.8-1.2-4a5.7 5.7 0 013.9 4z"/></svg>www.kestrelservicesltd.co.uk</li>
    </ul>
    <address class="address">
      Kestrel Services Ltd<br>
      14 Mill Parade<br>
      Ashcombe Road<br>
      Sutton, SM12XY
    </address>
  </section>

  <section class="card card--back">
    <div class="brand"><span class="brand__dot"></span>KESTREL SERVICES</div>
    <p class="tagline">Plumbing and Heating Services</p>
  </section>
</body>
</html>
```